Personal Travel Advisor needs Business Cards

UPDATED INFORMATION:
I have attached a sample of the script I would to use for "Travel"
Specialties are updated to: Culinary & Wine, Golf, Food, Cruising, River Cruising

I need a business card for my new company - Lena Orwick Travel - which I can also use as a logo.

I specialize in culinary & wine, golf, river cruising, select destinations and group travel.
The design should convey the value of my expertise and personalized services.

Target Market(s)

Target market is varied but most likely will be 40+ years.

I need to build a client base so need to be inclusive, but would like to draw in affluent travelers who value their time, and my expertise.

Groups can be any demographic - groups of golfers, wine club, sports fan trips, etc.

Industry/Entity Type

Business

Requirements
Must have
• Must find a non- prominent way to display the following information:

"Affiliated as an independent contractor with Bellhaven Travel"
and
"CST #4637215-84"

Nice to have
• The design should be striking but elegant with a modern look and feel

One side of the card could be in a solid color or black?

I like the idea of Lena Orwick being in a font and Travel being in a handwritten script...but I do not want this idea to inhibit your design.
Should not have
• I do not want any ships, planes, or other typical travel illustrations in the design.

```html
<!DOCTYPE html>
<html lang="en">
<head>
<meta charset="UTF-8">
<title>Lena Orwick Travel — Business Card</title>
<link rel="stylesheet" href="https://fonts.googleapis.com/css2?family=Josefin+Sans:wght@300;400&display=swap">
<style>
  :root {
    --backdrop: #2e2926;
    --card-black: #121212;
    --card-edge: #1c1c1c;
    --brand-red: #e0262b;
    --brand-silver: #b9bcc0;
    --detail-grey: #c8c8c8;
    --pattern-tone: #1f1f21;
  }
  * { margin: 0; padding: 0; box-sizing: border-box; }
  html, body {
    width: 1200px;
    height: 1000px;
    overflow: hidden;
    background: var(--backdrop);
    font-family: "Josefin Sans", sans-serif;
  }
  .canvas {
    width: 1200px;
    height: 1000px;
    display: flex;
    flex-direction: column;
    align-items: center;
    justify-content: center;
    gap: 40px;
  }
  .card {
    position: relative;
    width: 820px;
    height: 446px;
    background: radial-gradient(ellipse at 50% 45%, #222 0%, var(--card-black) 70%);
    border: 1px solid var(--card-edge);
    overflow: hidden;
  }
  .brand-name {
    font-weight: 300;
    letter-spacing: 1px;
    white-space: nowrap;
  }
  .card--front .brand-name {
    position: absolute;
    left: 0; right: 0;
    top: 180px;
    text-align: center;
    font-size: 56px;
    color: var(--brand-red);
  }
  .card--back .pattern {
    position: absolute;
    inset: 0;
    background: linear-gradient(180deg, var(--pattern-tone) 0%, #151515 100%);
  }
  .card--back .divider {
    position: absolute;
    left: 418px;
    top: 150px;
    width: 2px;
    height: 130px;
    background: linear-gradient(180deg, transparent, #000 30%, #000 70%, transparent);
    box-shadow: 6px 0 14px rgba(0,0,0,0.7);
  }
  .card--back .brand-name {
    position: absolute;
    left: 58px;
    top: 190px;
    font-size: 33px;
    color: var(--brand-silver);
  }
  .contact-list {
    position: absolute;
    left: 478px;
    top: 176px;
    list-style: none;
    font-size: 14px;
    font-weight: 300;
    color: var(--detail-grey);
    line-height: 25px;
    letter-spacing: 0.4px;
  }
  .fine-print {
    position: absolute;
    bottom: 40px;
    font-size: 11.5px;
    font-weight: 300;
    color: var(--detail-grey);
    letter-spacing: 0.3px;
  }
  .fine-print--licence { left: 30px; }
  .fine-print--affiliation { right: 30px; }
</style>
</head>
<body>
  <main class="canvas">
    <section class="card card--front" aria-label="Card front">
      <p class="brand-name">Lena Orwick Travel</p>
    </section>

    <section class="card card--back" aria-label="Card back">
      <div class="pattern" role="img" aria-label="Faint dark grey diamond lattice pattern across the card"></div>
      <div class="divider"></div>
      <p class="brand-name">Lena Orwick Travel</p>
      <ul class="contact-list">
        <li>Address: P.O Box 472 Ferndale VIC. 3918</li>
        <li>Email: hello@orwickmail.com</li>
        <li>Web: www.lenaorwicktravel.com</li>
        <li>Mobile: 0298 564 117</li>
      </ul>
      <p class="fine-print fine-print--licence">CST #4637215-84</p>
      <p class="fine-print fine-print--affiliation">Affiliated as an independent contractor with Bellhaven Travel</p>
    </section>
  </main>
</body>
</html>
```